Vitamin design-two ranges zephLUMA and kessarineLUMA

Need attractive unique packaging for a range of multivitamins and minerals starting with zephLUMA which aids cognitive function. Also there is a product we also want to produce which is called kessarineluma so we would like the design to be readily adjusted to fit this product also. KessarineLUMA design should reflect natural, fruit and vegetable content . We would like two variants on same basic design. One to reflect Zephluma and one to fit Kessarineluma. The brand is
Corvantaluma and the word luma should be prominent in the design.

Target Market(s)

US market

Industry/Entity Type

Vitamin

Requirements
Must have
• Company will send me template that design needs to fit into and packaging needs to have room for product ingredients and details. Also the brand must be transferable. We are looking to create a range of vitamins around the name corvantaluma. This is the first in a range so we would like the word "luma" in zephluma to be prominent.
Nice to have
• Something bright and appealing, eye catching and unique. Transferable design that fits both products and transferable to some others
• I'll email specifications from company around size of labels and regulations but here are some basics
• ZephLUMA capsules - label size 2.5 x6 for both 30 and 60 count.Bottle
• 30ct 100cc / 60ct 120cc
• Kessarine LUMA Label size 3x8 for 90ct bottle 300c
Should not have
• No claims of 100% natural or definitive claims

```html
<!DOCTYPE html>
<html lang="en">
<head>
<meta charset="utf-8">
<title>zephLUMA and kessarineLUMA labels</title>
<link rel="stylesheet" href="https://fonts.googleapis.com/css2?family=Open+Sans:wght@600;700;800&display=swap">
<style>
  :root {
    --page: #ffffff;
    --navy-deep: #0b2450;
    --navy: #15427e;
    --white: #ffffff;
    --cream: #fff8d6;
    --sun: #ffd34d;
    --orange: #f39a1e;
    --leaf-dark: #2c7a1c;
    --berry: #c9461c;
  }
  * { box-sizing: border-box; margin: 0; padding: 0; }
  html, body { width: 1200px; height: 979px; overflow: hidden; background: var(--page); }
  .canvas { position: relative; width: 1200px; height: 979px; font-family: "Open Sans", Arial, sans-serif; }

  .label { position: absolute; border-radius: 6px; overflow: hidden; }

  .brand { position: absolute; left: 0; right: 0; text-align: center;
    font-family: "Open Sans", Arial, sans-serif; font-weight: 800; letter-spacing: 0.5px; }
  .product-name { position: absolute; left: 0; right: 0; text-align: center;
    font-family: "Open Sans", Arial, sans-serif; font-weight: 800; line-height: 1; white-space: nowrap; }
  .count { position: absolute; left: 0; right: 0; text-align: center; font-weight: 700; line-height: 1.35; }

  /* zephLUMA */
  .label--zeph { left: 165px; top: 375px; width: 294px; height: 420px;
    background: linear-gradient(180deg, var(--navy) 0%, var(--navy-deep) 60%, #08193a 100%); }
  .label--zeph .brand { top: 46px; font-size: 13px; color: var(--white); }
  .label--zeph .product-name { top: 92px; font-size: 44px; color: var(--white); }
  .label--zeph .visual { position: absolute; left: 26px; top: 192px; width: 136px; height: 150px;
    border-radius: 50% 45% 20% 20%;
    background: radial-gradient(circle at 55% 40%, #2f7fd0 0%, #14396e 70%, #0b2450 100%); }
  .label--zeph .benefits { position: absolute; left: 170px; top: 204px; width: 120px; list-style: none;
    color: var(--white); font-weight: 700; font-size: 13.5px; line-height: 1.4; }
  .label--zeph .count { top: 376px; color: var(--white); font-size: 12px; }

  /* kessarineLUMA */
  .label--kess { left: 645px; top: 291px; width: 411px; height: 534px;
    background: linear-gradient(180deg, var(--cream) 0%, #fff1b0 55%, var(--sun) 100%); }
  .label--kess .brand { top: 54px; font-size: 15px; color: var(--leaf-dark); }
  .label--kess .product-name { top: 100px; font-size: 46px; color: var(--orange); }
  .label--kess .visual { position: absolute; left: 20px; top: 212px; width: 371px; height: 190px; border-radius: 40px;
    background: radial-gradient(ellipse at 50% 55%, #7bbf3a 0%, #d9472b 45%, #f4a321 75%, rgba(255,241,176,0) 100%); }
  .label--kess .count { top: 440px; font-size: 20px; }
  .label--kess .count-qty { color: var(--leaf-dark); }
  .label--kess .count-type { color: var(--berry); }
</style>
</head>
<body>
<main class="canvas">

  <section class="label label--zeph">
    <div class="brand">CORVANTALUMA</div>
    <h1 class="product-name">zephLUMA</h1>
    <div class="visual" role="img" aria-label="Blue profile illustration of a head with a glowing brain"></div>
    <ul class="benefits">
      <li>Supports Focus</li>
      <li>Mental Clarity</li>
      <li>and Healthy</li>
      <li>Mental Energy</li>
      <li>Mental Focus</li>
    </ul>
    <p class="count">30 Vegetable Capsules<br>Dietary Supplement</p>
  </section>

  <section class="label label--kess">
    <div class="brand">CORVANTALUMA</div>
    <h1 class="product-name">KessarineLUMA</h1>
    <div class="visual" role="img" aria-label="Photograph of fresh fruit and vegetables: broccoli, tomatoes, peppers, grapes and leafy greens"></div>
    <p class="count"><span class="count-qty">30 Vegetable Capsules</span><br><span class="count-type">Dietary Supplement</span></p>
  </section>

</main>
</body>
</html>
```